Baby Led Weaning App complete design

I want to develop a new app and I need full design for it, including screens, toolbars, icons, images, logo,etc.
The app is aiming to show the User information about baby led weaning, with theory and guidelines and it should also contain a section with recipes for baby lead weaning.

Industry/Entity Type
Baby
Requirements
Must have
- Full design for the app, including screens, toolbars, icons, images, logo,etc.
- The app will be used on smartphones and tablets so design should consider different screen sizes.

Nice to have
- The app is mainly for mums with babys. The design should be bright, happy (positive) and easy to use.
- It would be good to have nice images of babys feeding themselves (no bottle milk). The images in the documents provided need to be replaced.
- Colurs should be gender neutral (not specific to girl or boy).

Should not have
- The should not look too serious or cold.
- Nothing that can be interpreted as negative, heavy, complicated or sad.

```html
<!DOCTYPE html>
<html lang="en">
<head>
<meta charset="utf-8">
<title>Baby Led Weaning – Home</title>
<link rel="stylesheet" href="https://fonts.googleapis.com/css2?family=Roboto:wght@400;500;700&family=Playfair+Display:ital,wght@1,900&display=swap">
<style>
  :root {
    --page-bg: #efeeee;
    --yellow: #efe034;
    --ink: #1c1c1c;
    --white: #ffffff;
    --mint: #c9f3ee;
    --card: #f7f7f7;
    --grid: #e4e4e4;
    --muted: #6d6d6d;
    --badge: #2fb45a;
    --photo-a: #d9d23a;
    --photo-b: #2a2a26;
  }
  * { box-sizing: border-box; margin: 0; padding: 0; }
  html, body { width: 1200px; height: 744px; overflow: hidden; }
  body {
    background: var(--page-bg);
    font-family: "Roboto", Arial, sans-serif;
    display: flex; align-items: center; justify-content: center;
  }
  .app-screen {
    width: 390px; height: 700px;
    background: var(--grid);
    display: flex; flex-direction: column;
    overflow: hidden;
  }
  .hero {
    position: relative;
    height: 236px;
    background: var(--yellow);
    flex: none;
  }
  .hero__menu { position: absolute; left: 20px; top: 22px; }
  .hero__bell { position: absolute; right: 20px; top: 18px; }
  .hero__title {
    position: absolute; top: 26px; left: 0; right: 0;
    text-align: center; color: var(--white);
    font-size: 15px; font-weight: 500; letter-spacing: 0.5px;
  }
  .hero__photo {
    position: absolute; left: 40px; top: 72px;
    width: 170px; height: 150px;
    background: linear-gradient(90deg, var(--photo-a) 0 30%, var(--photo-b) 30% 62%, var(--photo-a) 62%);
  }
  .hero__headline {
    position: absolute; left: 222px; top: 88px;
    font-family: "Playfair Display", Georgia, serif;
    font-style: italic; font-weight: 900;
    font-size: 40px; color: var(--ink); line-height: 1;
  }
  .hero__tag {
    position: absolute; left: 214px; top: 146px;
    background: var(--mint);
    font-size: 9px; color: var(--ink);
    padding: 6px 10px;
  }
  .menu-grid {
    flex: 1;
    display: grid;
    grid-template-columns: 1fr 1fr;
    grid-template-rows: 1fr 1.1fr 1fr;
    gap: 6px;
    padding: 6px;
  }
  .card {
    background: var(--card);
    padding: 14px 16px;
    display: flex; gap: 12px;
  }
  .card--wide { grid-column: 1 / 3; align-items: center; }
  .card--stack { flex-direction: column; justify-content: flex-end; }
  .card__title { font-size: 17px; font-weight: 700; color: var(--ink); margin-bottom: 4px; }
  .card__text { font-size: 10px; line-height: 1.35; color: var(--muted); }
  .icon { flex: none; }
</style>
</head>
<body>
  <main class="app-screen">
    <header class="hero">
      <svg class="hero__menu" width="22" height="18" viewBox="0 0 22 18" aria-label="Menu">
        <g stroke="#fff" stroke-width="2"><line x1="0" y1="2" x2="22" y2="2"/><line x1="0" y1="9" x2="22" y2="9"/><line x1="0" y1="16" x2="22" y2="16"/></g>
      </svg>
      <h1 class="hero__title">BABY LED WEANING</h1>
      <svg class="hero__bell" width="26" height="24" viewBox="0 0 26 24" aria-label="Notifications">
        <path d="M8 18 Q10 14 10 9 Q10 4 15 4 Q20 4 20 9 Q20 14 22 18 Z" fill="#fff"/>
        <circle cx="15" cy="20" r="2" fill="#fff"/>
        <circle cx="6" cy="6" r="4.5" fill="var(--badge)"/>
        <text x="6" y="8.5" font-size="6" fill="#fff" text-anchor="middle" font-family="Roboto, sans-serif">1</text>
      </svg>
      <div class="hero__photo" role="img" aria-label="Flat-lay photo of a coffee cup, a small green plant and a bowl of berries on a black strip"></div>
      <p class="hero__headline">foods</p>
      <p class="hero__tag">to feed baby before age 1</p>
    </header>

    <section class="menu-grid">
      <article class="card card--wide">
        <svg class="icon" width="56" height="50" viewBox="0 0 56 50" aria-hidden="true">
          <g stroke="var(--ink)" stroke-width="2" fill="none">
            <rect x="20" y="12" width="32" height="34" rx="3" fill="var(--yellow)"/>
            <rect x="22" y="5" width="28" height="8" rx="2" fill="var(--white)"/>
            <circle cx="36" cy="30" r="7" fill="var(--white)"/>
            <ellipse cx="7" cy="26" rx="5" ry="6" fill="var(--yellow)"/>
            <line x1="9" y1="32" x2="16" y2="47"/>
          </g>
        </svg>
        <div>
          <h2 class="card__title">Theory</h2>
          <p class="card__text">Lorem ipsum dolor sit amet, consectetur adipisicing elit, sed do eiusmod tempor incididunt</p>
        </div>
      </article>

      <article class="card card--stack">
        <svg class="icon" width="44" height="40" viewBox="0 0 44 40" aria-hidden="true">
          <g stroke="var(--ink)" stroke-width="2" fill="none">
            <path d="M4 22 A18 18 0 0 0 40 22 Z" fill="var(--yellow)"/>
            <line x1="2" y1="22" x2="42" y2="22"/>
            <path d="M16 4 V16 M12 4 V10 Q16 14 20 10 V4"/>
            <ellipse cx="28" cy="8" rx="4" ry="5" fill="var(--white)"/>
            <line x1="28" y1="13" x2="28" y2="20"/>
          </g>
        </svg>
        <div>
          <h2 class="card__title">How to start</h2>
          <p class="card__text">Lorem ipsum dolor sit amet, consectetur adipisicing elit,</p>
        </div>
      </article>

      <article class="card card--stack">
        <svg class="icon" width="44" height="40" viewBox="0 0 44 40" aria-hidden="true">
          <g stroke="var(--ink)" stroke-width="2" fill="none">
            <circle cx="22" cy="20" r="17" fill="var(--yellow)"/>
            <circle cx="22" cy="20" r="10" fill="var(--white)"/>
            <path d="M8 6 V34 M4 6 V12 Q8 16 12 12 V6"/>
            <ellipse cx="36" cy="12" rx="3.5" ry="6" fill="var(--white)"/>
            <line x1="36" y1="18" x2="36" y2="34"/>
          </g>
        </svg>
        <div>
          <h2 class="card__title">Recipes</h2>
          <p class="card__text">Lorem ipsum dolor sit amet, consectetur adipisicing elit,</p>
        </div>
      </article>

      <article class="card card--wide">
        <svg class="icon" width="50" height="46" viewBox="0 0 50 46" aria-hidden="true">
          <g stroke="var(--ink)" stroke-width="2" fill="none">
            <path d="M6 6 H40 V38 H10 Q6 38 6 42 Z" fill="var(--yellow)"/>
            <path d="M6 42 Q6 44 10 44 H42 V38"/>
            <line x1="40" y1="6" x2="42" y2="8"/>
            <line x1="42" y1="8" x2="42" y2="44"/>
          </g>
        </svg>
        <div>
          <h2 class="card__title">Guidelines</h2>
          <p class="card__text">Lorem ipsum dolor sit amet, consectetur adipisicing elit, sed do eiusmod</p>
        </div>
      </article>
    </section>
  </main>
</body>
</html>
```